Create a Business Card Design Project for a new logistics company

We need a business card designed for a new company in Australia.

Type of business is logistics/trucking.

Medium will be brushed black metal card that can/will be acid etched to a brushed steel silver, acid die cut and two printed colours of our choice which will be white and pantone orange.

We have hopes that the design will be simple, modern and represent with a quick glance what our company does.

Please read instructions carefully in must have box any questions please ask.

If you are interested in this job please look at other job that we have which is very similar with logo and design

Please have a look at the things that can be done with metals cards on google images for inspiration.

Target Market(s)

Men from 20yrs of age to 60yrs of age

Industry/Entity Type

Steel

Requirements
Must have
• Must Have:
- Front of card:

Must use the company logo and name provided as attachment (see below KVR-black-background-cmyk).
Logo grey will be etched, orange and white will be printed on card. Parts of the logo could even be die cut.

The word -Logistics anytime, anywhere- on front etched, printed or die cut.

detail needed on front or back depending on your design layout.

Name
position
email
mobile

all details can be on front if a nice design is etched on the back of card or to keep front simple you can put all detail on back of card, I will leave the lay out to you.

Colours in logo are

Pantone 144 C Orange
Pantone 11-0601 White
Pantone 7539 C Gray
Pantone 426 C Black

However black will be the base of black metal card. Gray will be replaced with the etching in card revealing the silver. Orange and white will be printed on card.

have fun!!
Nice to have
• The file attached called idea is just an example of what can be designed and etched into card. Google has many more idea's for metal business cards.
Should not have
• Please don't clutter the card
No fonts smaller then 7 points

```html
<!DOCTYPE html>
<html lang="en">
<head>
<meta charset="utf-8">
<title>KVR Industries – Business Cards</title>
<link rel="stylesheet" href="https://fonts.googleapis.com/css2?family=Open+Sans:wght@300;400;600;700&display=swap">
<style>
  :root {
    --backdrop: #2a1a12;
    --card-black: #15181b;
    --card-edge: #0c0e10;
    --orange: #f08a1c;
    --white: #f2f2f2;
    --silver: #a9abae;
    --silver-dark: #6f7275;
    --muted: #8d9094;
  }
  * { margin: 0; padding: 0; box-sizing: border-box; }
  html, body {
    width: 1200px; height: 900px; overflow: hidden;
    background: var(--backdrop);
    font-family: "Open Sans", Arial, sans-serif;
  }
  .canvas { position: relative; width: 1200px; height: 900px; }

  .card {
    position: absolute;
    background: var(--card-black);
    border: 1px solid var(--card-edge);
    box-shadow: 0 14px 30px rgba(0,0,0,.55);
  }
  .card--cover { left: 80px; top: 90px; width: 620px; height: 355px; }
  .card--details { left: 470px; top: 430px; width: 660px; height: 380px; }

  .brand { position: absolute; display: flex; align-items: center; gap: 12px; }
  .brand__dot {
    width: 26px; height: 26px; border-radius: 50%;
    background: var(--silver);
  }
  .brand__name {
    font-weight: 700; color: var(--orange);
    letter-spacing: 2px; line-height: 1;
  }
  .card--cover .brand { left: 150px; top: 150px; }
  .card--cover .brand__name { font-size: 46px; }
  .card--details .brand { left: 50px; top: 44px; }
  .card--details .brand__dot { width: 20px; height: 20px; }
  .brand--small .brand__name { font-size: 32px; }

  .tagline {
    position: absolute; right: 0; top: 200px;
    width: 250px; padding: 9px 0 9px 14px;
    border-top: 1px solid var(--orange);
    border-bottom: 1px solid var(--orange);
    color: var(--muted); font-size: 12px; font-weight: 600;
    letter-spacing: 1.5px; text-transform: uppercase;
  }

  .person { position: absolute; left: 60px; top: 165px; }
  .person__name { color: var(--white); font-weight: 700; font-size: 20px; letter-spacing: 1px; }
  .person__role { color: var(--silver); font-weight: 300; font-size: 14px; letter-spacing: .5px; }

  .contact {
    position: absolute; left: 135px; top: 240px;
    border-left: 1px solid var(--silver-dark);
    padding: 6px 0 6px 28px;
    display: flex; flex-direction: column; gap: 18px;
  }
  .contact__row { display: flex; align-items: center; gap: 22px; color: var(--muted); font-size: 15px; font-weight: 300; letter-spacing: 1px; }
  .contact__icon { width: 16px; height: 16px; flex: none; }
  .contact__at { color: var(--orange); font-size: 17px; width: 16px; text-align: center; font-weight: 400; }

  .emblem {
    position: absolute; right: 60px; top: 120px;
    font-weight: 700; font-size: 110px; line-height: 1;
    color: var(--silver-dark); letter-spacing: 4px;
  }
</style>
</head>
<body>
<main class="canvas">
  <section class="card card--cover" aria-label="Business card front">
    <div class="brand">
      <span class="brand__dot"></span>
      <span class="brand__name">KVR</span>
    </div>
    <p class="tagline">Logistics anytime, anywhere</p>
  </section>

  <section class="card card--details" aria-label="Business card contact side">
    <div class="brand brand--small">
      <span class="brand__dot"></span>
      <span class="brand__name">KVR</span>
    </div>
    <div class="person">
      <p class="person__name">Liam Carter</p>
      <p class="person__role">general manager</p>
    </div>
    <div class="contact">
      <p class="contact__row">
        <svg class="contact__icon" viewBox="0 0 16 16" aria-hidden="true">
          <rect x="4" y="1" width="8" height="14" rx="1.5" fill="none" stroke="#f08a1c" stroke-width="1.5"/>
          <line x1="7" y1="12.5" x2="9" y2="12.5" stroke="#f08a1c" stroke-width="1.5"/>
        </svg>
        <span>001 234 56789</span>
      </p>
      <p class="contact__row">
        <span class="contact__at">@</span>
        <span>carter@kvrfreight.com</span>
      </p>
    </div>
    <p class="emblem" aria-hidden="true">KVR</p>
  </section>
</main>
</body>
</html>
```